Striking new Advert required for Commercial Real Estate Agency

We need a a NEW newspaper advertisement for the marketing of a large commercial property (a Backpackers lodge)

Dimensions are to be width of 101mm and height of 100mm (10cms)

Our key design statement for this advert is clean, modern and minimalist design, with accents of 'HOT PINK' colour to remove it from looking too boring, perhaps in the area of the contact icons. The heirachy of the advert is outlined in the attached ADVERTISEMENT TEXT FILE.

Our company name is THE MERIDAL COLLECTIVE, and we want our brand to appear professional yet classy in it's design style (sort of like an advertising or design agency)

We have two logo options below, one more square in its layout (which we prefer) and the other more rectangular, which may be better suited for the layout. We are not adverse to the logo being reversed (white text on black), along with other key element areas such as the main advert heading and the "FOR SALE" part, and think this would be a good option.
There are two photos attached to be included in the advert.

We have attached an example of an old advert that we did, which we DID NOT LIKE, and which was for a smaller width than the one we need (it is only 65% of the width of this one). WE have also atached a file showing layout of some of our competitors adverts, which we dont think are too good either.

We are really open for ideas, but have time pressures, so please come back with any questions as soon as you can, if needed.

Thank you
Updates

Thank you for the great and diverse designs. There are a few standout options, but one style that we prefer most.

Target Market(s)

We are wanting this newspaper advertisement to attract interest from real estat e developers, investors and motel/lodge owners, along with other high nett worth individuals

Industry/Entity Type

Real Estate

Font styles to use
Serif
Sans Serif

Colors
1b1b1b
a54499
474747
fbfbfb

Requirements
Must have
• Clean modern look, predominantly monochromatic or black and white, with the hot pink accent somewhere, as mentioned above.
• All the contents of the TEXT provided, perhaps with additional space to add a little more if needed, Please advise if you think we dont have enough space for all of the TEXT
Should not have
• Script like fonts
• Cartoonish characters
• a 'cheap' look

```html
<!DOCTYPE html>
<html lang="en">
<head>
<meta charset="utf-8">
<title>For Sale – Harwell's Lodge</title>
<link rel="stylesheet" href="https://fonts.googleapis.com/css2?family=Fira+Sans+Extra+Condensed:wght@400;500;600;700&family=Arimo:wght@700&display=swap">
<style>
  :root {
    --ink: #1b1b1b;
    --pink: #a54499;
    --grey: #474747;
    --paper: #fbfbfb;
    --white: #ffffff;
  }
  * { margin: 0; padding: 0; box-sizing: border-box; }
  html, body { width: 1200px; height: 1188px; overflow: hidden; background: var(--ink); }
  .advert {
    position: relative;
    width: 1200px;
    height: 1188px;
    background: var(--ink);
    color: var(--white);
    font-family: "Fira Sans Extra Condensed", "Arial Narrow", sans-serif;
  }
  .headline {
    position: absolute;
    left: 28px;
    top: 8px;
    font-size: 108px;
    font-weight: 600;
    color: var(--pink);
    letter-spacing: 1px;
    line-height: 1.1;
  }
  .headline-divider {
    position: absolute;
    left: 447px;
    top: 24px;
    width: 3px;
    height: 84px;
    background: var(--white);
  }
  .property-title {
    position: absolute;
    left: 487px;
    top: 16px;
    font-size: 46px;
    font-weight: 600;
    line-height: 50px;
  }
  .hero-photo {
    position: absolute;
    left: 0;
    top: 135px;
    width: 780px;
    height: 562px;
    background: linear-gradient(160deg, #9fa9a4 0%, #d9d8d2 30%, #c3c1b9 55%, #6d7168 80%, #8c9a4e 100%);
  }
  .feature-panel {
    position: absolute;
    left: 748px;
    top: 135px;
    width: 446px;
    height: 562px;
    background: var(--pink);
  }
  .feature-photo {
    position: absolute;
    left: 17px;
    top: 17px;
    width: 413px;
    height: 276px;
    background: linear-gradient(170deg, #7ea6d8 0%, #b9cde6 35%, #e4e3de 55%, #6b7b4a 85%, #4e5d33 100%);
  }
  .feature-copy {
    position: absolute;
    left: 49px;
    top: 306px;
    width: 380px;
    font-size: 31px;
    font-weight: 600;
    line-height: 41px;
  }
  .key-details {
    position: absolute;
    left: 34px;
    top: 708px;
    width: 1140px;
    list-style: none;
    font-size: 31px;
    font-weight: 400;
    line-height: 45px;
  }
  .key-details li {
    position: relative;
    padding-left: 34px;
  }
  .key-details li::before {
    content: "";
    position: absolute;
    left: 2px;
    top: 17px;
    width: 14px;
    height: 14px;
    border-radius: 50%;
    background: var(--white);
  }
  .key-details sup { font-size: 18px; line-height: 0; }
  .tender-band {
    position: absolute;
    left: 0;
    top: 952px;
    width: 568px;
    height: 52px;
    background: var(--pink);
    padding-left: 37px;
    font-size: 36px;
    font-weight: 700;
    letter-spacing: 3px;
    line-height: 52px;
  }
  .agent-contact {
    position: absolute;
    left: 38px;
    top: 1018px;
    font-size: 34px;
    font-style: normal;
    line-height: 50px;
  }
  .agent-contact .agent-name { font-weight: 700; font-size: 36px; margin-left: 10px; }
  .contact-row { display: flex; align-items: center; gap: 10px; }
  .contact-row svg { flex: none; }
  .contact-row .spacer { width: 26px; }
  .brand {
    position: absolute;
    left: 760px;
    top: 990px;
    width: 420px;
    display: flex;
    align-items: center;
    gap: 18px;
  }
  .brand-dot {
    flex: none;
    width: 22px;
    height: 22px;
    border-radius: 50%;
    background: var(--white);
  }
  .brand-name {
    font-size: 44px;
    font-weight: 600;
    letter-spacing: 2px;
    line-height: 50px;
  }
  .website {
    position: absolute;
    left: 760px;
    top: 1134px;
    font-family: "Arimo", Arial, sans-serif;
    font-weight: 700;
    font-size: 25px;
    color: var(--pink);
    letter-spacing: 1px;
  }
</style>
</head>
<body>
<main class="advert">
  <header>
    <h1 class="headline">FOR SALE</h1>
    <div class="headline-divider"></div>
    <h2 class="property-title">Harwell’s Lodge, 42 Calloway Street,<br>Mount Ashby</h2>
  </header>

  <div class="hero-photo" role="img" aria-label="Aerial photo of the white two-storey lodge with car park and surrounding suburb"></div>

  <section class="feature-panel">
    <div class="feature-photo" role="img" aria-label="Photo of the lodge's white weatherboard facade and side path under blue sky"></div>
    <p class="feature-copy">This Old Beauty has served many, and is now ripe for development. One of Mt Ashby’s largest land areas, now offered with vacant possession, with key details being:</p>
  </section>

  <ul class="key-details">
    <li>Large Land area of 2076m<sup>2</sup> with elevated sunny position and great outlook + access from<br>Tennant Street</li>
    <li>Existing Backpackers Lodge of 970m<sup>2</sup> providing multiple rooms with amenity areas</li>
    <li>Four adjacent sites also available, taking total land area to 4452m<sup>2</sup>, an unprecedented Land<br>Offering in this popular cuity fringe location</li>
  </ul>

  <div class="tender-band">Now Selling by Closed Tender</div>

  <address class="agent-contact">
    <div class="contact-row">Contact the Sole Agent :<span class="agent-name">Daniel Morrow</span></div>
    <div class="contact-row">
      <svg width="24" height="22" viewBox="0 0 24 22" aria-hidden="true"><path d="M2 8c0-4 4-6 10-6s10 2 10 6l-4 1-1-3H7L6 9z" fill="#fff"/><rect x="4" y="11" width="16" height="9" rx="2" fill="#fff"/></svg>
      <span>(04) 555 0142</span>
      <span class="spacer"></span>
      <svg width="20" height="26" viewBox="0 0 20 26" aria-hidden="true"><rect x="3" y="1" width="14" height="24" rx="3" fill="none" stroke="#fff" stroke-width="2.5"/><circle cx="10" cy="20" r="1.6" fill="#fff"/></svg>
      <span>(021) 555 019</span>
    </div>
    <div class="contact-row">
      <svg width="26" height="18" viewBox="0 0 26 18" aria-hidden="true"><rect x="1.5" y="1.5" width="23" height="15" fill="none" stroke="#fff" stroke-width="2"/><path d="M2 2l11 8 11-8" fill="none" stroke="#fff" stroke-width="2"/></svg>
      <span>daniel@meridalcollective.co.nz</span>
    </div>
  </address>

  <div class="brand">
    <span class="brand-dot"></span>
    <span class="brand-name">THE MERIDAL<br>COLLECTIVE</span>
  </div>
  <div class="website">www.meridalcollective.co.nz</div>
</main>
</body>
</html>
```